Cellular Repair Retail Store Flyer/Postcards

We are looking for a good flyer for us to print and distribute as well as post on various web sites. Our company name is "Handset Mend Crew" and we repair a wide range of cellular phones from Zelphones to Zelpads, Korvane's,,QT's, Brenwick, and PDX. In general if you have a cell phone we repair it. Cellular repairs is the primary focus however we are also an accessory superstore with 1'000's of choices of phone cases for all model phones. Historically these phone cases have all been aftermarket however now there are a number of brands. I'll attach a few so we have the ability to use some branded logo's on the flyer. Not all the graphics need to be used that we are providing. Again the flyer's main objective is, 1) Cellular Repairs, 2) Our location & pic of building (I have one attached but i'll have a new one within 24 hours and 3) Cellular Accessory Superstore with 1,000's of case. The address to our location is 4817 S 19th Street, Milwaukee, Wisconsin 53221. Anytime we use our address we state "2 Blocks South of 19th & Vermont" (popular intersection in the market). So i'm not sure what approach to go... but I figured i'd provide a bunch of stuff for you to pick from. Naturally let's not make the flyer too busy but if we hit the 3 main deal points we will be good. Attached are; some pics of attractive phone cases, a few cellular accessory brands such as Lynx Shell, Varmoda, Gripwrap, LuMonte, Fortrex etc. These logo's may add a nice appeal given they are national companies. For your reference and to be listed on the flyer is our web site; www.handsetmendcrew.com

Industry/Entity Type

Cell Phone

Requirements
Must have
• This advertisement will be used for the NPDS Each Home Bulk Post so we need to make the flyer with the following measurements in mind; 6.25" x 9"
Nice to have
• In addition to repairing phones we need to promote we buy used and broken smart phones. Repairs done on site with certified technicians.

```html
<!DOCTYPE html>
<html lang="en">
<head>
<meta charset="utf-8">
<title>Handset Mend Crew – Fix Your Phone Today</title>
<link rel="stylesheet" href="https://fonts.googleapis.com/css2?family=Montserrat:wght@700;800&family=Didact+Gothic&family=Josefin+Sans:wght@400;600&display=swap">
<style>
  :root {
    --white: #ffffff;
    --sky: #1b9bf0;
    --sun: #f1c232;
    --badge: #f0b323;
    --navy: #1e3a53;
    --brand: #1c3f63;
    --ink: #2f3338;
    --muted: #222222;
    --frame: #dfe4ea;
  }
  * { margin: 0; padding: 0; box-sizing: border-box; }
  html, body { width: 837px; height: 1200px; overflow: hidden; background: var(--white); }
  .flyer { position: relative; width: 837px; height: 1200px; overflow: hidden; background: var(--white); font-family: "Josefin Sans", sans-serif; }

  .brand { position: absolute; right: 50px; top: 38px; text-align: right; }
  .brand-name { font-family: "Montserrat", sans-serif; font-weight: 800; font-size: 38px; color: var(--brand); letter-spacing: -0.5px; line-height: 1; }
  .brand-url { margin-top: 20px; font-size: 18px; color: var(--muted); }

  .hero-band { position: absolute; left: 0; top: 310px; width: 837px; height: 366px; background: var(--sky); }
  .device-photo { position: absolute; left: 54px; top: 160px; width: 540px; height: 358px; border-radius: 18px;
    background: linear-gradient(135deg, #1c1f24 0%, #4a5563 45%, #20242a 100%); }

  .call-badge { position: absolute; left: 565px; top: 422px; width: 266px; height: 60px; background: var(--badge);
    display: flex; align-items: center; justify-content: center; gap: 12px;
    font-size: 28px; color: var(--muted); }
  .call-badge svg { width: 30px; height: 30px; }

  .headline { position: absolute; left: 0; top: 508px; width: 837px; font-weight: normal; }
  .headline-fix { text-align: center; font-family: "Montserrat", sans-serif; font-weight: 800; font-size: 64px; color: var(--white); line-height: 1; }
  .headline-rest { margin-top: 4px; padding-left: 57px; font-family: "Didact Gothic", sans-serif; font-size: 74px; line-height: 1; white-space: nowrap; }
  .headline-rest .dark { color: var(--ink); }
  .headline-rest .light { color: var(--white); }

  .services-band { position: absolute; left: 0; top: 684px; width: 837px; height: 257px; background: var(--sun); }
  .service-list { position: absolute; left: 84px; top: 32px; list-style: none; }
  .service-list li { position: relative; padding-left: 29px; font-size: 21px; color: var(--muted); line-height: 38.5px; }
  .service-list li::before { content: ""; position: absolute; left: 0; top: 14px; width: 8px; height: 8px; border-radius: 50%; background: var(--muted); }
  .service-list .accessory { font-weight: 600; }

  .store-photo { position: absolute; left: 583px; top: 700px; width: 216px; height: 207px; border: 3px solid var(--white);
    background: linear-gradient(160deg, #e7eef6 0%, #b9c6d6 55%, #8f9aa8 100%); }

  .location-band { position: absolute; left: 0; top: 941px; width: 837px; height: 259px; background: var(--navy); }
  .building-photo { position: absolute; left: 40px; top: 901px; width: 348px; height: 232px; border: 7px solid var(--frame);
    background: linear-gradient(180deg, #8fb8e6 0%, #c8d9ea 45%, #e8e3da 70%, #9a8f84 100%); }
  .location { position: absolute; left: 434px; top: 976px; color: var(--white); font-style: normal; }
  .location-landmark { font-size: 28px; line-height: 38px; padding-left: 7px; }
  .location-address { margin-top: 14px; font-size: 21px; line-height: 30px; }
</style>
</head>
<body>
<div class="flyer">
  <div class="hero-band"></div>

  <header class="brand">
    <div class="brand-name">Handset Mend Crew</div>
    <div class="brand-url">www.handsetmendcrew.com</div>
  </header>

  <div class="device-photo" role="img" aria-label="Phone, tablet and smartphone with cracked screens"></div>

  <div class="call-badge">
    <svg viewBox="0 0 24 24" aria-hidden="true"><path fill="#2b2b2b" d="M6.6 10.8a15.1 15.1 0 0 0 6.6 6.6l2.2-2.2a1 1 0 0 1 1-.25 11.4 11.4 0 0 0 3.6.57 1 1 0 0 1 1 1V20a1 1 0 0 1-1 1A17 17 0 0 1 3 4a1 1 0 0 1 1-1h3.5a1 1 0 0 1 1 1c0 1.25.2 2.45.57 3.57a1 1 0 0 1-.25 1z"/></svg>
    <span>414-555-0183</span>
  </div>

  <h1 class="headline">
    <div class="headline-fix">FIX</div>
    <div class="headline-rest"><span class="dark">YOUR PHONE</span> <span class="light">TODAY</span></div>
  </h1>

  <section class="services-band">
    <ul class="service-list">
      <li>Water Damage</li>
      <li>Broken glass and LCDs</li>
      <li>Battery replacement and charging port</li>
      <li>Camera and home button replacement</li>
      <li class="accessory">Accessory Superstore – 1,000's of cases</li>
    </ul>
  </section>

  <div class="store-photo" role="img" aria-label="Store interior with walls of phone cases and accessory displays"></div>

  <section class="location-band"></section>
  <div class="building-photo" role="img" aria-label="Exterior of the single-storey store building with black awnings"></div>

  <address class="location">
    <div class="location-landmark">2 Blocks South of<br>19th &amp; Vermont</div>
    <div class="location-address">4817 S 19th Street,<br>Milwaukee, Wisconsin 53221</div>
  </address>
</div>
</body>
</html>
```